VarloPeak

Need a 6 page template designed in Layered PSD for a house cleaning company.

Target Market(s)

People who are selling their homes and need house cleaning

Industry/Entity Type

House cleaning

Number of Pages Required

5+ page

Font styles to use
Sans Serif

Requirements
Must have
• Please see the zip file included with the brief. It has a document with detailed instructions.

```html
<!DOCTYPE html>
<html lang="en">
<head>
<meta charset="utf-8">
<title>VarloPeak – Barrie Area Move-In, Move-Out &amp; Pre-Sale Cleaning</title>
<link href="https://fonts.googleapis.com/css2?family=Oswald:wght@500;600&family=Poppins:wght@400;500;600&display=swap" rel="stylesheet">
<style>
:root{
  --navy:#1f3f8c;
  --navy-deep:#1a3577;
  --green:#6cbd3c;
  --green-dark:#5aa82f;
  --ink:#1f2533;
  --muted:#3c4250;
  --white:#ffffff;
  --photo-warm:#c9b9a4;
  --photo-cool:#b8c2cf;
}
*{margin:0;padding:0;box-sizing:border-box}
html,body{width:1200px;height:5153px;overflow:hidden;background:var(--white)}
body{font-family:"Poppins",sans-serif;color:var(--ink);font-size:13px;line-height:1.62}
.page{position:relative;width:1200px;height:5153px}
section,header,footer{position:absolute;left:0;width:1200px}
.abs{position:absolute}
h1,h2,h3{font-family:"Oswald",sans-serif;font-weight:600;line-height:1.3}
.heading{color:var(--navy);font-size:32px}
.eyebrow{color:var(--green);font-size:12px;letter-spacing:.5px;text-transform:uppercase;margin-bottom:10px}
p+p{margin-top:14px}
.btn{display:inline-block;background:var(--green);color:var(--white);font-weight:600;font-size:13px;padding:11px 28px;text-decoration:none;border-radius:2px}
.ring{position:absolute;border:2.5px solid var(--green);border-radius:50%;width:22px;height:22px}
.photo{position:absolute;overflow:hidden}
.circle{border-radius:50%}

/* header */
.site-header{top:0;height:130px}
.brand{left:62px;top:40px;display:flex;align-items:center;gap:8px;font-family:"Poppins",sans-serif;font-weight:600;font-size:24px;color:var(--navy)}
.brand-dot{width:14px;height:14px;background:var(--green);border-radius:50%}
.nav{left:290px;top:52px;display:flex;gap:30px;font-size:12px}
.nav a{color:var(--navy);text-decoration:none}
.nav a.active{color:var(--green)}
.hdr-phone{left:796px;top:44px;width:164px;height:36px;background:var(--green);color:#fff;font-size:12px;display:flex;align-items:center;justify-content:center;gap:8px;border-radius:2px}
.hdr-cta{left:976px;top:44px;width:164px;height:36px;background:var(--navy);color:#fff;font-size:12px;display:flex;align-items:center;justify-content:center;border-radius:2px}

/* hero */
.hero{top:130px;height:568px;background:linear-gradient(90deg,var(--navy) 0%,var(--navy) 38%,#8aa0c6 70%,#d9dde3 100%)}
.hero-photo{left:440px;top:0;width:760px;height:568px;background:linear-gradient(90deg,rgba(31,63,140,0) 0%,rgba(200,205,212,.55) 40%,#e2e2e0 100%)}
.hero-copy{left:62px;top:84px;width:450px;color:#fff}
.hero-copy h1{font-size:25px;margin-bottom:18px}
.hero-copy p{font-size:11px;line-height:1.75}
.hero-copy .btn{margin-top:34px}

/* services */
.services{top:698px;height:500px}
.services h2{font-size:38px}
.svc-list{list-style:none;display:grid;grid-template-columns:226px 200px;row-gap:14px;font-size:15px;margin:18px 0 26px}
.svc-list li::before{content:"+ ";color:var(--green)}

/* split rows */
.split-copy{width:540px;font-size:13px}
.split-copy h2{margin-bottom:22px}
.split-copy .btn{margin-top:38px}

/* realtors */
.realtors{top:2272px;height:572px;background:linear-gradient(90deg,var(--navy) 0%,var(--navy) 40%,#6d84b6 62%,#d3d7dd 100%)}
.realtors h2{font-size:38px;color:#fff;margin-bottom:16px}
.realtors-copy{left:62px;top:80px;width:420px;color:#fff;font-size:13px}
.realtors-copy .btn{margin-top:28px}
.realtors-note{margin-top:38px;font-style:italic;font-weight:600;text-decoration:underline;font-size:15px;line-height:1.6}

/* audiences */
.audiences{top:3454px;height:526px}
.aud-panel{position:absolute;top:0;width:400px;height:526px}
.aud-panel h3{position:absolute;left:0;width:400px;text-align:center;color:#fff;font-size:25px;bottom:60px}
.aud-mid{left:400px;background:var(--navy);color:#fff;text-align:center;padding:46px 46px 0}
.aud-mid h3{position:static;font-size:25px;margin-bottom:24px;width:auto}
.aud-mid p{font-size:12.5px;line-height:1.7}
.aud-mid .btn{margin-top:40px}

/* cta */
.cta{top:3980px;height:616px;text-align:center}
.cta h2{font-size:36px;color:var(--navy);line-height:1.2}
.cta p{font-size:13px;width:740px;margin:30px auto 0}
.cta .btn{margin-top:52px;font-size:16px;padding:14px 34px}

/* footer */
.site-footer{top:4596px;height:507px;background:var(--navy);color:#fff}
.site-footer h4{font-family:"Oswald",sans-serif;font-weight:600;font-size:21px;margin-bottom:16px}
.foot-col{position:absolute;top:74px;font-size:12.5px}
.foot-col ul{list-style:none}
.foot-col li{margin-bottom:10px;line-height:1.4}
.foot-col li::before{content:"+ ";color:var(--green)}
.areas{display:grid;grid-template-columns:154px 160px}
.contact-row{display:flex;gap:12px;margin-bottom:22px;align-items:flex-start}
.footer-ring{position:absolute;border:2px solid rgba(255,255,255,.18);border-radius:50%;width:28px;height:28px}
.copyright{top:5103px;height:50px;background:var(--green);color:#fff;font-size:11.5px}
.copyright .abs{top:17px}
.social{right:62px;display:flex;gap:10px}
.social span{display:block;width:16px;height:16px;border:1.5px solid #fff;border-radius:3px}
</style>
</head>
<body>
<div class="page">

<header class="site-header">
  <div class="abs brand"><span class="brand-dot"></span>VarloPeak</div>
  <nav class="abs nav">
    <a class="active" href="#">Home</a><a href="#">Services</a><a href="#">What's Included</a><a href="#">For Realtors</a><a href="#">Blog</a>
  </nav>
  <div class="abs hdr-phone">
    <svg width="14" height="14" viewBox="0 0 24 24" fill="none" stroke="#fff" stroke-width="2"><path d="M22 16.9v3a2 2 0 0 1-2.2 2 19.8 19.8 0 0 1-8.6-3.1 19.5 19.5 0 0 1-6-6A19.8 19.8 0 0 1 2.1 4.2 2 2 0 0 1 4.1 2h3a2 2 0 0 1 2 1.7c.1 1 .4 1.9.7 2.8a2 2 0 0 1-.5 2.1L8 9.9a16 16 0 0 0 6 6l1.3-1.3a2 2 0 0 1 2.1-.4c.9.3 1.8.6 2.8.7a2 2 0 0 1 1.7 2z"/></svg>
    +100 555 0199
  </div>
  <div class="abs hdr-cta">Get a Free Estimate</div>
</header>

<section class="hero">
  <div class="photo hero-photo" role="img" aria-label="Cleaner in blue apron and orange gloves wiping a floor with a pink cloth"></div>
  <div class="abs hero-copy">
    <h1>The Only Barrie Area Cleaning Service That Specializes in Deep Pre-Sale, Move-In, &amp; Move-Out House Cleanings</h1>
    <p>Welcome to the only Barrie area cleaning service specializing in deep move-in, move-out, and pre-sale house cleanings.</p>
    <p>Moving in or out of a home can be daunting with so much to organize and prepare. Cleaning is often the last thing on your mind, but it's essential to sell your home quickly and to have a clean, hygienic environment in your new home for you and your family when you move in.</p>
    <p>Whether you're moving in or out of a Barrie area home, apartment, or rental property, our Barrie area Pre-Sale, Move-In, and Move-Out Deep Cleaning Services are the perfect solution for you.</p>
    <a class="btn" href="#">Get a Free Estimate</a>
  </div>
</section>

<section class="services">
  <div class="photo circle" style="left:210px;top:142px;width:300px;height:300px;background:radial-gradient(circle at 50% 60%,#6cbd3c 0 70%,#5aa82f 100%)" role="img" aria-label="Smiling cleaner in blue apron holding a caddy of cleaning supplies"></div>
  <span class="ring" style="left:128px;top:266px"></span>
  <span class="ring" style="left:766px;top:100px"></span>
  <span class="ring" style="left:1058px;top:226px;width:18px;height:18px"></span>
  <div class="abs" style="left:580px;top:160px">
    <h2 class="heading" style="font-size:38px">Cleaning Services We Offer</h2>
    <ul class="svc-list"><li>Pre-Sale Cleaning</li><li>Move-In Cleaning</li><li>Move-Out Cleaning</li><li>Junk Removal</li></ul>
    <a class="btn" href="#">Get a Free Estimate</a>
  </div>
</section>

<section class="presale" style="top:1198px;height:540px">
  <div class="abs split-copy" style="left:62px;top:36px">
    <div class="eyebrow">Pre-Sale Cleanings</div>
    <h2 class="heading">Are You Putting Your Barrie Area<br>Home Up for Sale?</h2>
    <p>First impressions matter, and a clean and fresh home can make a huge difference. At VarloPeak, we specialize in deep cleaning services that will get your home in tip-top shape for potential buyers.</p>
    <p>Not only will a move-out deep cleaning make your home more attractive to potential buyers, but it can also increase its value. A well-maintained home is a valuable asset that can command a higher price on the Barrie area market.</p>
    <p>Let us take the stress out of preparing your home for sale. Our Barrie area pre-sale deep cleaning services are tailored to your needs and can be scheduled at a time that works for you. We guarantee your satisfaction and promise to leave your home sparkling clean.</p>
    <a class="btn" href="#">Get a Free Estimate</a>
  </div>
  <div class="photo circle" style="left:698px;top:58px;width:400px;height:400px;background:radial-gradient(circle,#eceef0,#cfd4da)" role="img" aria-label="Cleaner vacuuming a bright living room with a canister vacuum"></div>
  <span class="ring" style="left:664px;top:128px;width:18px;height:18px"></span>
  <span class="ring" style="left:1114px;top:268px"></span>
</section>

<section class="movein" style="top:1738px;height:534px">
  <div class="photo circle" style="left:70px;top:42px;width:400px;height:400px;background:radial-gradient(circle,#e9e7e3,#bfc5cc)" role="img" aria-label="Cleaner in yellow gloves sweeping a floor beside a cleaning cart"></div>
  <span class="ring" style="left:452px;top:56px"></span>
  <span class="ring" style="left:34px;top:172px;width:18px;height:18px"></span>
  <div class="abs split-copy" style="left:618px;top:30px">
    <div class="eyebrow">Move-In Cleanings</div>
    <h2 class="heading">Take the Stress Out of Your Move &amp;<br>Have Your Home Sparkling Clean<br>Before You Move In</h2>
    <p>Moving doesn't have to be a stressful experience. Let us take the hassle out of your move and ensure your new Barrie home is clean, fresh, and ready for you to settle in.</p>
    <p>Our Barrie area move-in deep cleaning Service is designed so that you can start your new chapter with a spotless and hygienic environment. Our experienced and skilled cleaners will work diligently to ensure that every nook and cranny of your new Barrie home is perfectly cleaned.</p>
    <a class="btn" href="#">Get a Free Estimate</a>
  </div>
</section>

<section class="realtors">
  <div class="photo" style="left:560px;top:0;width:640px;height:572px;background:linear-gradient(90deg,rgba(31,63,140,0),rgba(225,226,228,.8) 45%,#e6e4e0)" role="img" aria-label="Realtor welcoming a happy couple into a bright home"></div>
  <div class="abs realtors-copy">
    <h2>Attention Realtors!!!</h2>
    <p>As a Barrie area realtor, you know that buying or selling a home can be stressful for your clients.</p>
    <p>Here at VarloPeak, we want to help make that process as smooth as possible.</p>
    <p>That's why we're excited to introduce our Barrie area move-in &amp; move-out deep cleaning services as a value-added service for your clients.</p>
    <a class="btn" href="#">Click Here For More Info</a>
    <p class="realtors-note">Let us take the hassle out of your client's move and ensure their Barrie home is deep-cleaned, fresh, and ready.</p>
  </div>
</section>

<section class="moveout" style="top:2844px;height:610px">
  <div class="photo circle" style="left:64px;top:94px;width:424px;height:424px;background:radial-gradient(circle,#e4ddd3,#b9ada0)" role="img" aria-label="Person mopping the floor of a bright kitchen"></div>
  <span class="ring" style="left:62px;top:130px;width:20px;height:20px"></span>
  <span class="ring" style="left:492px;top:380px;width:18px;height:18px"></span>
  <div class="abs split-copy" style="left:618px;top:126px">
    <div class="eyebrow">Move-Out Cleanings</div>
    <h2 class="heading">Cleaned &amp; Ready for The Next Occupants</h2>
    <p>Looking for a professional move-out cleaning service to ensure that your property is left sparkling clean and ready for the next occupants? Look no further than our expert team of cleaning professionals!</p>
    <p>At VarloPeak, we provide move-out cleaning services to homeowners and tenants throughout the Barrie area. Our team of experienced and fully trained cleaners will work tirelessly to ensure your property is left in pristine condition when you move out so that you can focus on your move without any added stress.</p>
    <a class="btn" href="#">Get a Free Estimate</a>
  </div>
</section>

<section class="audiences">
  <div class="aud-panel photo" style="left:0;background:linear-gradient(180deg,#b88a55 0%,#8a6a4c 55%,#2a2c3a 100%)" role="img" aria-label="Family making a roof shape with their arms in their home">
    <h3>Move-Out Cleaning for<br>Homeowners</h3>
  </div>
  <div class="aud-panel aud-mid">
    <h3>Move-Out Cleaning for<br>Renters</h3>
    <p>Are you moving out of your Barrie area rental property soon and need to ensure that the property is left sparkling clean to get your security deposit back?</p>
    <p>Don't let the stress of move-out cleaning get in the way of getting your security deposit back.</p>
    <p>Contact us today to schedule your move-out cleaning service, and let us help you leave your rental in pristine condition when you move out.</p>
    <a class="btn" href="#">Get a Free Estimate</a>
  </div>
  <div class="aud-panel photo" style="left:800px;background:linear-gradient(180deg,#8e96a3 0%,#5b6270 55%,#22262f 100%)" role="img" aria-label="Smiling property manager holding up a set of keys">
    <h3>Move Out Cleaning for<br>Landlords &amp; Property Managers</h3>
  </div>
</section>

<section class="cta">
  <span class="abs" style="left:584px;top:100px;width:32px;height:32px;border-radius:50%;background:var(--green)"></span>
  <span class="ring" style="left:222px;top:96px"></span>
  <span class="ring" style="left:1022px;top:200px;width:28px;height:28px"></span>
  <span class="ring" style="left:1128px;top:368px"></span>
  <span class="ring" style="left:174px;top:422px;width:30px;height:30px"></span>
  <span class="abs" style="left:64px;top:238px;color:var(--green);font-size:22px">+</span>
  <span class="abs" style="left:908px;top:470px;color:var(--green);font-size:22px">+</span>
  <h2 style="position:absolute;left:0;width:1200px;top:182px">The Only Barrie Area Cleaning Service That<br>Specializes in Deep Pre-Sale, Move-In &amp;<br>Move-Out House Cleanings</h2>
  <div style="position:absolute;left:0;width:1200px;top:308px">
    <p style="margin-top:0">Whether you're moving into or out of a Barrie area home, apartment, or rental property, our Barrie area Pre-Sale, Move-In, and Move-Out Deep Cleaning Services are the perfect solution for you. Contact us today to schedule an appointment, and let us take care of the daunting task of having your home deep cleaned so that you can enjoy your new Barrie area home from day one.</p>
    <a class="btn" href="#">Get a Free Estimate</a>
  </div>
</section>

<footer class="site-footer">
  <span class="footer-ring" style="left:594px;top:222px"></span>
  <span class="footer-ring" style="left:1138px;top:264px;width:24px;height:24px"></span>
  <span class="footer-ring" style="left:734px;top:372px"></span>
  <span class="footer-ring" style="left:32px;top:408px;width:20px;height:20px"></span>
  <div class="foot-col" style="left:62px">
    <h4>Areas We Serve</h4>
    <ul class="areas">
      <li>Alliston</li><li>Minesing</li><li>Angus</li><li>New Lowell</li><li>Barrie</li><li>Orillia</li><li>Coldwater</li><li>Oro-Medonte</li><li>Collingwood</li><li>Shanty Bay</li><li>Creemore</li><li>Springwater</li><li>Horseshoe Valley</li><li>Stayner</li><li>Innisfil</li><li>Wasaga</li><li>Midland</li><li>And everywhere<br>&nbsp;&nbsp;&nbsp;in between</li>
    </ul>
  </div>
  <div class="foot-col" style="left:480px">
    <h4>Availability</h4>
    <ul>
      <li>Open 7 Days a Week (Monday-Sunday)</li>
      <li>Hours 8:00 am - 9:00 pm</li>
      <li>Evenings &amp; Weekends (Yes)</li>
    </ul>
  </div>
  <div class="foot-col" style="left:904px">
    <h4>Contact Us</h4>
    <div class="contact-row">
      <svg width="18" height="20" viewBox="0 0 24 24" fill="none" stroke="#6cbd3c" stroke-width="2"><path d="M12 22s7-7 7-12a7 7 0 0 0-14 0c0 5 7 12 7 12z"/><circle cx="12" cy="10" r="2.5"/></svg>
      <span>123 Your Address Goes Here,<br>Barrie, Canada</span>
    </div>
    <div class="contact-row">
      <svg width="18" height="18" viewBox="0 0 24 24" fill="none" stroke="#6cbd3c" stroke-width="2"><path d="M22 16.9v3a2 2 0 0 1-2.2 2 19.8 19.8 0 0 1-8.6-3.1 19.5 19.5 0 0 1-6-6A19.8 19.8 0 0 1 2.1 4.2 2 2 0 0 1 4.1 2h3a2 2 0 0 1 2 1.7c.1 1 .4 1.9.7 2.8a2 2 0 0 1-.5 2.1L8 9.9a16 16 0 0 0 6 6l1.3-1.3a2 2 0 0 1 2.1-.4c.9.3 1.8.6 2.8.7a2 2 0 0 1 1.7 2z"/></svg>
      <span>+100 555 0199</span>
    </div>
    <div class="contact-row">
      <svg width="20" height="16" viewBox="0 0 24 18" fill="none" stroke="#6cbd3c" stroke-width="2"><rect x="1" y="1" width="22" height="16" rx="1"/><path d="M1 2l11 8 11-8"/></svg>
      <span>hello@varlopeak.com</span>
    </div>
  </div>
</footer>

<div class="copyright" style="position:absolute;left:0;width:1200px">
  <div class="abs" style="left:62px">Copyright© 2023 VarloPeak. All rights reserved.</div>
  <div class="abs social"><span></span><span></span></div>
</div>

</div>
</body>
</html>
```